BRIXEN San Felipe - For all your home service needs.

I need a web site designed for my new business called BRIXEN San Felipe. This business is for the repair and servicing of home appliances and air conditioning systems and for plumbing and electrical repairs at residences. We will offer 1 year service contracts that provide for unlimited service calls and repairs of the equipment that is enrolled in the program. The business is located in San Felipe, Baja CA, Mexico which has a large population of retired American and Canadians. These are our target audience, not the Mexican population.

The business is an outgrowth of another business we own in San Felipe called Corvana Management Services which has been in business for 7 years and is well known and highly regarded in the community. The company is owned and operated by two Mexican nationals and an American who are all full time residents of San Felipe.

Our business model is the same as an American company called Brixen whose web site is https://www.quellorhome.net/.

I already have a domain on Netvolta called www.brixenbaja.com and need a web design to populate this domain. We also have a Logo designed which I will upload for you.

Target Market(s)

The target audience is American and Canadian retirees who own homes and live in San Felipe either part time or full time.

Industry/Entity Type

Air Conditioning

Requirements
Must have
• The web site must have a home page, about us, service contracts, repairs, AC sales, Renewals, Quotes and Contact us pages. The information will be very similar to that shown for https://www.quellorhome.net/.
Nice to have
• San Felipe is a desert community with an ocean (the gulf of California) so the design should incorporate some desert motifs and some seaside motifs. Also, should have some thoughts about how are services will make living in San Felipe worry free and enable the clients to enjoy life. One number to call for all their home service needs.
Should not have
• Do not have anything that belittles Mexico or Mexicans.

```html
<!DOCTYPE html>
<html lang="en">
<head>
<meta charset="utf-8">
<title>Brixen San Felipe – Home Services</title>
<link href="https://fonts.googleapis.com/css2?family=Source+Sans+3:ital,wght@0,400;0,600;0,700;1,400&display=swap" rel="stylesheet">
<style>
:root{
  --red:#b5121b;
  --red-dark:#8e0f15;
  --heading:#9b1119;
  --text:#4a4a4a;
  --muted:#6b6b6b;
  --nav-top:#555559;
  --nav-bottom:#2b2b2e;
  --panel:#f4f4f4;
  --border:#dcdcdc;
  --footer:#47464b;
  --white:#ffffff;
}
*{margin:0;padding:0;box-sizing:border-box}
html,body{width:1200px;height:1116px;overflow:hidden}
body{
  font-family:"Source Sans 3",sans-serif;
  color:var(--text);
  position:relative;
  background:linear-gradient(180deg,#fbf8f4 0%,#efe6da 30%,#b9c4c8 45%,#8a98a0 55%,#b89986 75%,#8d6e5e 100%);
}
.top-strip{position:absolute;left:0;top:0;width:1200px;height:7px;background:var(--red)}
.page{position:absolute;left:172px;top:7px;width:857px;height:1109px;background:var(--white)}
.abs{position:absolute}

/* header */
.brand{left:180px;top:48px;display:flex;align-items:center;gap:8px}
.brand-mark{width:40px;height:40px;border-radius:50%;background:var(--red)}
.brand-name{font-size:34px;font-weight:700;color:var(--red);line-height:1}
.hours{left:561px;top:50px;font-size:40px;font-weight:700;color:var(--red);line-height:1;letter-spacing:-1px}
.call-label{left:662px;top:52px;font-size:14px;font-weight:600;color:#555;letter-spacing:.3px}
.call-number{left:662px;top:67px;font-size:21px;font-weight:600;color:#e2231a}
.divider{left:808px;top:49px;width:1px;height:47px;background:#ddd}
.follow{left:827px;top:69px;font-size:8px;color:#555;text-transform:uppercase}
.socials{left:880px;top:60px;display:flex;gap:2px}
.socials span{width:26px;height:26px;border-radius:50%;display:block}

/* nav */
.main-nav{left:181px;top:123px;width:840px;height:39px;border-radius:3px;
  background:linear-gradient(180deg,var(--nav-top),var(--nav-bottom));
  display:flex;align-items:center;justify-content:space-around;padding:0 20px}
.main-nav a{color:var(--white);font-size:11px;font-weight:700;text-decoration:none;text-transform:uppercase}

/* estimate form */
.estimate{left:180px;top:176px;width:229px;height:318px;background:var(--red-dark);border-radius:3px;overflow:hidden}
.estimate h2{height:36px;background:linear-gradient(180deg,#d21a24,var(--red));color:var(--white);
  font-size:13.5px;font-weight:700;text-align:center;line-height:36px}
.field{position:absolute;left:17px;width:197px;height:23px;background:var(--white);border-radius:2px;
  font-size:7px;color:#555;padding:8px 9px;text-transform:uppercase}
.field.area{height:49px}
.submit{position:absolute;left:122px;top:279px;width:92px;height:25px;border-radius:3px;
  background:linear-gradient(180deg,#5a5a5e,#2c2c2f);color:var(--white);font-size:10px;font-weight:700;
  text-align:center;line-height:25px}

/* slider */
.hero{left:429px;top:177px;width:591px;height:318px;border-radius:3px;overflow:hidden;
  background:linear-gradient(120deg,#e9d5bd 0%,#d3b89a 35%,#6d7688 65%,#2f3752 100%)}
.hero-caption{position:absolute;left:0;bottom:0;width:100%;height:70px;background:rgba(40,40,44,.8);
  color:var(--white);font-size:12.5px;font-weight:700;text-transform:uppercase;line-height:22px;padding:13px 17px}
.hero-arrows{position:absolute;right:0;top:227px;width:43px;height:21px;background:#2b2b2e;display:flex}
.hero-arrows svg{flex:1}

/* section headings */
.section-title{font-size:17px;font-weight:600;color:var(--heading);text-transform:uppercase}
.col-title{font-size:12.5px;font-weight:600;color:var(--heading);text-transform:uppercase}

/* why choose */
.why{left:181px;top:550px;width:228px;height:247px;background:var(--panel);border:1px solid var(--border);border-radius:2px}
.qualities{position:absolute;left:20px;top:13px;display:grid;grid-template-columns:100px 100px;row-gap:7px;list-style:none}
.qualities li{font-size:10px;color:var(--heading);height:14px}
.qualities li::before{content:"› ";color:#555}
.why p{position:absolute;left:21px;top:109px;width:195px;font-size:9.5px;line-height:15.4px;color:var(--text)}
.btn{position:absolute;border-radius:3px;background:linear-gradient(180deg,#5a5a5e,#2c2c2f);
  color:var(--white);font-size:10px;font-weight:700;text-align:center;text-transform:uppercase;
  box-shadow:0 1px 2px rgba(0,0,0,.35)}
.why .btn{left:95px;top:201px;width:112px;height:29px;line-height:29px}

/* testimonials */
.testi-arrows{left:381px;top:818px;font-size:12px;color:#555;letter-spacing:5px}
.testimonial{left:181px;top:849px;width:228px;height:152px;border:1px solid var(--border);border-radius:2px;background:var(--white)}
.quote-mark{position:absolute;font-size:30px;color:#cfcfcf;font-family:Georgia,serif;line-height:1}
.testimonial p{position:absolute;left:34px;top:30px;width:170px;font-size:9px;line-height:15.4px}
.author{position:absolute;left:34px;top:115px;font-size:9px;color:var(--heading);text-transform:uppercase}
.posted{position:absolute;left:34px;top:131px;font-size:8.5px;font-style:italic;color:#777}

/* welcome */
.photo{border-radius:1px}
.welcome-text{font-size:9px;line-height:15.4px;color:var(--text)}
.service-list{list-style:none;font-size:10px;color:var(--heading)}
.service-list li::before{content:"»  ";color:var(--heading)}
.col-text{font-size:9px;line-height:15.4px;width:178px}
.col-btn{width:86px;height:24px;line-height:24px;font-weight:600}

/* footer */
.site-footer{left:181px;top:1038px;width:840px;height:78px;background:var(--footer);border-radius:3px 3px 0 0}
.footer-nav{position:absolute;left:0;width:100%;top:22px;display:flex;justify-content:center;gap:0;font-size:8px;color:var(--white);text-transform:uppercase}
.footer-nav span{padding:0 18px;border-left:1px solid #aaa;line-height:9px}
.footer-nav span:first-child{border-left:0}
.copyright{position:absolute;left:0;width:100%;top:45px;text-align:center;font-size:8px;color:var(--white);text-transform:uppercase}
</style>
</head>
<body>
<div class="top-strip"></div>
<div class="page"></div>

<header>
  <div class="abs brand"><span class="brand-mark"></span><span class="brand-name">Brixen</span></div>
  <div class="abs hours">24/7</div>
  <div class="abs call-label">CALL US :</div>
  <div class="abs call-number">(555) 013-7742</div>
  <div class="abs divider"></div>
  <div class="abs follow">Follow us :</div>
  <div class="abs socials" aria-label="Social links">
    <span style="background:#2e6fb6"></span>
    <span style="background:#1f7fa8"></span>
    <span style="background:#45a9dc"></span>
    <span style="background:#e89a1c"></span>
    <span style="background:#3a3a3a"></span>
  </div>
</header>

<nav class="abs main-nav">
  <a href="#">Home</a><a href="#">About Us</a><a href="#">Service Contracts</a><a href="#">Repairs</a>
  <a href="#">AC Sales</a><a href="#">Renewals</a><a href="#">Quotes and Contact Us</a>
</nav>

<section class="abs estimate">
  <h2>GET A FREE ESTIMATE!</h2>
  <div class="field" style="top:48px">Full name :</div>
  <div class="field" style="top:82px">Your email :</div>
  <div class="field" style="top:116px">Your phone :</div>
  <div class="field" style="top:150px">Property zip code :</div>
  <div class="field" style="top:184px">Do you have an active contract :</div>
  <div class="field area" style="top:218px">How can we help you? :</div>
  <div class="submit">SUBMIT</div>
</section>

<section class="abs hero" role="img" aria-label="Photo of a smiling technician repairing a kitchen faucet with a wrench">
  <div class="hero-arrows">
    <svg viewBox="0 0 21 21"><path d="M12 7l-3 3.5 3 3.5" fill="none" stroke="#fff" stroke-width="1.2"/></svg>
    <svg viewBox="0 0 21 21"><path d="M9 7l3 3.5-3 3.5" fill="none" stroke="#fff" stroke-width="1.2"/></svg>
  </div>
  <div class="hero-caption">We do the repair and servicing of home appliances and air conditioning systems and for plumbing and electrical repairs at residences.</div>
</section>

<h2 class="abs section-title" style="left:183px;top:515px">Why Choose Us</h2>
<section class="abs why">
  <ul class="qualities">
    <li>Licensed</li><li>Insured</li><li>Certified</li><li>Reliable</li>
    <li>Trusted</li><li>Reputable</li><li>Stable</li><li>Affordable</li>
  </ul>
  <p>t is a long established fact that a reader will be distracted by the readable content of a page when looking at its layout. The point of using Lorem Ipsum is that it has a more-or-less normal distribution...</p>
  <div class="btn">Read More</div>
</section>

<h2 class="abs section-title" style="left:183px;top:815px">Testimonials</h2>
<div class="abs testi-arrows">‹ ›</div>
<section class="abs testimonial">
  <span class="quote-mark" style="left:14px;top:16px">“</span>
  <p>It is a long established fact that a reader will be distracted by the readable content of a page when looking at its layout. The point of using normal distribution...</p>
  <span class="quote-mark" style="left:190px;top:86px">”</span>
  <div class="author">Marcus Ellery</div>
  <div class="posted">Posted on 20 Aug 2013</div>
</section>

<h2 class="abs section-title" style="left:435px;top:517px">Welcome to Brixen</h2>
<div class="abs photo" role="img" aria-label="Photo of a plumber in a blue cap working under a sink" style="left:435px;top:552px;width:194px;height:93px;background:linear-gradient(135deg,#e4e6ea,#b9c2cf 55%,#3e5f9a)"></div>
<p class="abs welcome-text" style="left:648px;top:553px;width:370px">It is a long established fact that a reader will be distracted by the readable content of a page when looking at its layout. The point of using Lorem Ipsum is that it has a more-or-less normal distribution of letters, as opposed to using 'Content here, content here', making it look like readable English. Many desktop publishing packages and web page editors now use Lorem Ipsum as their default model text, and a search for 'lorem ipsum' will uncover many web sites still in their infancy. Various versions have evolved over the years...</p>
<p class="abs welcome-text" style="left:437px;top:661px;width:580px">It is a long established fact that a reader will be distracted by the readable content of a page when looking at its layout. The point of using Lorem Ipsum is that it has a more-or-less normal distribution of letters, as opposed...</p>
<ul class="abs service-list" style="left:439px;top:707px;line-height:23px">
  <li>Repair and servicing of home appliances</li><li>air conditioning systems</li>
</ul>
<ul class="abs service-list" style="left:679px;top:707px;line-height:23px">
  <li>plumbing</li><li>electrical repairs</li>
</ul>

<h3 class="abs col-title" style="left:435px;top:777px">Residential Services</h3>
<div class="abs" role="img" aria-label="Illustration of a roofer silhouetted against an orange sunset" style="left:436px;top:806px;width:177px;height:84px;background:radial-gradient(circle at 35% 35%,#ffe14a,#f59a12 50%,#b4400a)"></div>
<p class="abs col-text" style="left:436px;top:901px">It is a long established fact that a reader will be distracted by the readable content of a page when looking at its layout. The point of using normal distribution of letters...</p>
<div class="btn col-btn" style="left:437px;top:974px">Read More</div>

<h3 class="abs col-title" style="left:639px;top:777px">Community Services</h3>
<div class="abs" role="img" aria-label="Photo of gloved hands hammering a wooden board" style="left:640px;top:806px;width:177px;height:84px;background:linear-gradient(135deg,#8a6a52,#c7a27c 50%,#5b4536)"></div>
<p class="abs col-text" style="left:640px;top:901px">It is a long established fact that a reader will be distracted by the readable content of a page when looking at its layout. The point of using normal distribution of letters...</p>
<div class="btn col-btn" style="left:641px;top:974px">Read More</div>

<h3 class="abs col-title" style="left:844px;top:777px">Repairs</h3>
<div class="abs" role="img" aria-label="Photo of an electrician in a red cap working on wall wiring" style="left:845px;top:806px;width:176px;height:84px;background:linear-gradient(135deg,#f2f2f0,#e7d7c4 45%,#2d5cb0 75%,#d92a24)"></div>
<p class="abs col-text" style="left:844px;top:901px">It is a long established fact that a reader will be distracted by the readable content of a page when looking at its layout. The point of using normal distribution of letters...</p>
<div class="btn col-btn" style="left:845px;top:974px">Read More</div>

<footer class="abs site-footer">
  <div class="footer-nav">
    <span>Home</span><span>About Us</span><span>Service Contracts</span><span>Repairs</span>
    <span>AC Sales</span><span>Renewals</span><span>Quotes and Contact Us</span>
  </div>
  <div class="copyright">Copyright © 2013.BRIXEN. All rights reserved.</div>
</footer>
</body>
</html>
```